Market online tutoring + Back to School + give Support for students school work K to 12 Grade

To promote my tutoring business online need to create a two sided flyer. Need to get the attention of parents and educators who looking for help to support the digital learning of their students due to COVID-19 lock down. I need to project and differentiate that we offer support for online school with individualized learning . We tutor Elementary to High school students on all subjects you may take a look at my website qnacademyga.com for additional info and also I can provide
Updates

Hi All Due to Covid, we were unable to work on this project on time as originally planned. We were given an extension until March 15 and we will complete it by then. Sorry for any inconvenience and Thank you for your support. -QN Academy

Target Market(s)

Parents and students

Industry/Entity Type

Education

Requirements
Must have
• For online less fine print on the first page. The phone number and support text message. Back to School , Support Online learning KEV/NUR test prep should have some focus
Nice to have
• Discuss the platform We created a platform with live instructor interaction, virtual classroom, instructional videos, assessments, and practice to support every individual student’s need. We are confident in our ability to provide the most effective distance learning experience.
Should not have
• too much clunky and packed with content. Should be easy to read with color

```html
<!DOCTYPE html>
<html lang="en">
<head>
<meta charset="utf-8">
<title>QN Academy – Two-sided Flyer</title>
<link href="https://fonts.googleapis.com/css2?family=PT+Serif:wght@400;700&family=Open+Sans:wght@400;600&display=swap" rel="stylesheet">
<style>
:root{
  --red:#b31b2c;
  --teal:#0f4756;
  --ink:#1d1d1f;
  --paper:#ffffff;
  --stage:#0c5560;
  --muted:#3a3a3a;
  --serif:"PT Serif", Georgia, serif;
  --sans:"Open Sans", Arial, sans-serif;
}
*{box-sizing:border-box;margin:0;padding:0}
html,body{width:1200px;height:2400px;overflow:hidden;background:var(--stage)}
.page{position:absolute;left:210px;width:780px;height:1104px;background:var(--paper);overflow:hidden;box-shadow:0 6px 24px rgba(0,0,0,.35)}
.front{top:40px}
.back{top:1220px}
.abs{position:absolute}
.brand{position:absolute;display:flex;align-items:center;gap:14px}
.brand-mark{width:58px;height:58px;background:var(--teal)}
.brand-name{font-family:var(--serif);color:var(--teal);font-size:30px;line-height:1;font-weight:400}
.photo{position:absolute}
.headline{position:absolute;left:20px;width:340px;text-align:center;font-family:var(--serif)}
.h-love{top:160px;font-size:62px;color:var(--ink);line-height:1}
.h-teach{top:225px;font-size:56px;color:var(--red);font-weight:700;line-height:1}
.h-quote{top:292px;font-size:14px;color:var(--ink);line-height:1.3}
.h-online{top:342px;font-size:46px;color:var(--ink);line-height:1}
.h-fine{top:398px;font-size:33px;color:var(--ink);line-height:1}
.band{position:absolute;left:0;height:54px;display:flex;align-items:center;padding-left:74px;font-family:var(--serif);font-size:28px;color:#fff}
.band-teal{background:var(--teal);clip-path:polygon(0 0,100% 0,94% 100%,0 100%)}
.band-red{background:var(--red);clip-path:polygon(0 0,94% 0,100% 100%,0 100%)}
.copy{position:absolute;font-family:var(--sans);font-size:10px;line-height:1.42;color:var(--muted);text-align:justify}
.copy-stack{position:absolute;display:flex;flex-direction:column;gap:12px}
.copy-stack .copy{position:static}
.rule{position:absolute;height:3px}
.rule::after{content:"";position:absolute;top:-4px;width:11px;height:11px;border-radius:50%;background:inherit}
.rule-end::after{right:-4px}
.rule-start::after{left:-4px}
.tagbar{position:absolute;left:26px;width:724px;background:#111;color:#fff;font-family:var(--serif);display:flex;align-items:center;justify-content:center}
.contact-line{position:absolute;left:0;width:780px;top:1046px;text-align:center;font-family:var(--serif);font-size:19px;letter-spacing:5px;color:var(--ink)}
.title-red{position:absolute;left:46px;top:59px;width:361px;height:56px;background:var(--red);color:#fff;font-family:var(--serif);font-size:38px;display:flex;align-items:center;justify-content:center}
.services-title{position:absolute;top:398px;left:0;width:780px;text-align:center;font-family:var(--serif);font-size:40px;color:var(--teal)}
.services-title b{color:var(--red)}
.strap{position:absolute;left:12px;width:756px;top:458px;height:28px;background:var(--teal);color:#fff;font-family:var(--serif);font-size:12px;display:flex;align-items:center;justify-content:center;letter-spacing:.3px}
.service{position:absolute;width:300px}
.service-head{display:flex;align-items:center;gap:10px;font-family:var(--serif);font-size:20px;color:var(--red);line-height:1.1}
.service-icon{flex:none;width:40px;height:40px;border:2px solid var(--teal);border-radius:50%;display:flex;align-items:center;justify-content:center}
.service p{margin:10px 0 0 12px;font-family:var(--sans);font-size:10.5px;line-height:1.45;color:var(--muted);text-align:justify}
.footer{position:absolute;left:26px;top:1010px;width:724px;height:58px;background:#111;color:#fff;display:flex;align-items:center}
.footer-cell{flex:1;padding:0 24px;font-family:var(--sans);font-size:10px;line-height:1.6}
.footer-phone{flex:1;text-align:center;font-family:var(--serif);font-size:20px;letter-spacing:4px;border-left:1px solid #555;border-right:1px solid #555}
.footer-web{letter-spacing:.5px}
</style>
</head>
<body>

<section class="page front">
  <div class="brand" style="left:40px;top:26px">
    <span class="brand-mark"></span>
    <span class="brand-name">QN<br>ACADEMY</span>
  </div>

  <svg class="abs" style="left:340px;top:0" width="440" height="480" viewBox="0 0 440 480">
    <polygon points="100,40 260,20 440,60 440,160 300,0 170,0" fill="var(--teal)"/>
    <polygon points="360,0 440,0 440,110" fill="var(--red)" opacity=".9"/>
    <polygon points="78,230 140,88 180,300 120,420" fill="var(--teal)"/>
    <polygon points="30,370 130,390 60,455" fill="var(--red)"/>
  </svg>
  <div class="photo" role="img" aria-label="Photo of a teacher helping two smiling students with their reading"
       style="left:430px;top:60px;width:340px;height:380px;clip-path:polygon(25% 0,100% 0,100% 75%,75% 100%,20% 100%,0 50%);background:linear-gradient(135deg,#e9d4c9 0%,#d986a8 45%,#7c5a46 100%)"></div>

  <div class="headline h-love">WE LOVE</div>
  <div class="headline h-teach">TEACHING</div>
  <div class="headline h-quote">Teaching is the greatest act of optimism”<br>-Maren Holloway</div>
  <div class="headline h-online">For online</div>
  <div class="headline h-fine">LESS FINE PRINT</div>

  <div class="band band-teal" style="top:462px;width:410px">WHO ARE WE?</div>

  <p class="copy" style="left:36px;top:530px;width:710px">QN Academy in Cedar Falls/Maple Ridge Georgia, is a private tutoring center which provides group coaching in Math, Reading, KEV Preparation, and Computer Programming for kids. We are proud to offer a curriculum that is truly unique, providing a strong focus on advanced coaching in Math and Reading. We also provide effective coaching for standardized tests like KEV, BRT, etc. We step away from the regular coaching method and implement effective problem solving techniques and critical thinking skills to help achieve stronger academic results.</p>
  <p class="copy" style="left:36px;top:606px;width:340px">QN Academy strives to improve your children's academic achievements and analytical problem solving skills. We believe that stretching a child's mind through critical thinking skills, accelerated academic programs, and exposure to computer programming and robotics at an early age will help them rise to their true potential. Children who learn programming and robotics can implement the knowledge gained in other challenging tasks and desired achievement.</p>
  <p class="copy" style="left:406px;top:606px;width:340px">QN Academy provides every student with personal guidance. We give students the platform and tools needed to conquer, to build confidence in them, to excel in their goals, and to achieve their dreams. By attending our programs, each student is able to truly internalize the concepts when the teacher introduces them at their level of understanding. This focused coaching allows the student to master concepts faster</p>
  <div class="rule rule-start" style="left:520px;top:752px;width:260px;background:var(--teal)"></div>

  <div class="band band-red" style="top:770px;width:370px">WHO ARE WE?</div>
  <p class="copy" style="left:36px;top:840px;width:400px">Mobile First has become a key strategy for the Corporate World; isn't it therefore important to introduce Mobile First in education too? Being ardent users of mobile devices, our students can be innovators of the mobile applications of the future. Should we not prepare them to create these apps too? QN Academy is introducing a set of courses for Mobile App Development that will prepare your students for their future in mobile application design and development.</p>
  <div class="photo" role="img" aria-label="Photo of a row of students working at computers in a classroom"
       style="left:455px;top:770px;width:285px;height:180px;background:linear-gradient(120deg,#c9a98d 0%,#8fa4b8 50%,#3f5f80 100%)"></div>
  <div class="rule rule-end" style="left:420px;top:966px;width:300px;background:var(--red)"></div>

  <div class="tagbar" style="top:984px;height:44px;font-size:15.5px">Back to School , Support Online learning KEV/NUR test prep should have some focus</div>
  <div class="contact-line">555-014-2290 / www.qnacademyga.com</div>
</section>

<section class="page back">
  <div class="title-red">Our Academy</div>
  <div class="brand" style="left:470px;top:50px">
    <span class="brand-mark"></span>
    <span class="brand-name">QN<br>ACADEMY</span>
  </div>
  <div class="rule rule-start" style="left:492px;top:148px;width:288px;background:var(--red)"></div>

  <div class="copy-stack" style="left:34px;top:130px;width:400px">
    <p class="copy">QN Academy in Cedar Falls/Maple Ridge, Georgia is a private tutoring center which provides group coaching in Math, Reading, KEV Preparation, and Computer Programming for kids. We are proud to offer a curriculum that is truly unique, providing a strong focus on advanced coaching in Math and Reading. We also provide effective coaching for standardized tests like KEV, BRT, etc. We step away from the regular coaching method and implement effective problem solving techniques and critical thinking skills to help our children achieve stronger academic results.</p>
    <p class="copy">Our approach includes comprehensive evaluations done to determine his/her current levels within the subject(s) of interest. Based on the assessment outcome, we will create an individualized program for each child. Our teaches will work with your child and go over any weak areas to cover subject materials. Once we help your student meet or surpass the required skill level the challenges will be replaced by a newfound confidence and love towards learning.</p>
  </div>

  <div class="photo" role="img" aria-label="Photo of a child reaching toward a hanging model of the planets in a classroom"
       style="left:466px;top:168px;width:256px;height:168px;background:linear-gradient(135deg,#9fb4cf 0%,#d8a27a 55%,#7d3a2c 100%)"></div>
  <div class="rule rule-end" style="left:446px;top:356px;width:290px;background:var(--red)"></div>

  <div class="services-title">Our <b>SERVICES</b></div>
  <div class="strap">WE CATER TO STUDENTS' NEEDS IN A VARIETY OF FORMS, FROM GROUP CLASSES TO ONE-ON-ONE TUTORING.</div>

  <div class="service" style="left:52px;top:508px">
    <div class="service-head"><span class="service-icon"><svg width="20" height="20" viewBox="0 0 20 20" fill="none" stroke="var(--teal)" stroke-width="1.6"><rect x="2" y="2" width="16" height="16"/><path d="M10 2v16M2 10h16M5 6h3M13 6h3M14.5 4.5v3M5 14h3M13 13h3M13 15h3"/></svg></span>Mathematics (Georgia<br>Standard of Education)</div>
    <p>Our uniquely designed custom enrichment math courses will stretch our students mind and help them achieve higher grades.</p>
  </div>
  <div class="service" style="left:52px;top:632px">
    <div class="service-head"><span class="service-icon"><svg width="20" height="20" viewBox="0 0 20 20" fill="none" stroke="var(--teal)" stroke-width="1.6"><path d="M4 16l2-5 8-8 3 3-8 8zM4 16l5-2"/></svg></span>Writing (GSE)</div>
    <p>Our uniquely designed custom enrichment reading &amp; writing courses will stretch our students mind and help them achieve higher grades.</p>
  </div>
  <div class="service" style="left:52px;top:738px">
    <div class="service-head"><span class="service-icon"><svg width="20" height="20" viewBox="0 0 20 20" fill="none" stroke="var(--teal)" stroke-width="1.6"><circle cx="10" cy="8" r="5"/><path d="M8 14h4M8 17h4"/></svg></span>Critical Thinking</div>
    <p>Critical thinking is identifying and evaluating evidence to guide decision making. Our critical thinking classes focuses on improving critical thinking skills.</p>
  </div>
  <div class="service" style="left:52px;top:844px">
    <div class="service-head"><span class="service-icon"><svg width="20" height="20" viewBox="0 0 20 20" fill="none" stroke="var(--teal)" stroke-width="1.6"><rect x="4" y="6" width="12" height="10"/><path d="M10 2v4M7 10h1M12 10h1M7 13h6"/></svg></span>Robotics</div>
    <p>Robots play a major role in space exploration, industry automation, medical research and many other industries. Introducing the basics of robotics to kids widens their understanding of machines and opens new avenues for creativity and innovation.</p>
  </div>

  <div class="service" style="left:420px;top:508px">
    <div class="service-head"><span class="service-icon"><svg width="20" height="20" viewBox="0 0 20 20" fill="none" stroke="var(--teal)" stroke-width="1.6"><path d="M2 5c3-1 6-1 8 1 2-2 5-2 8-1v11c-3-1-6-1-8 1-2-2-5-2-8-1zM10 6v11"/></svg></span>Reading (GSE)</div>
    <p>Our uniquely designed custom enrichment reading &amp; writing courses will stretch our students mind and help them achieve higher grades.</p>
  </div>
  <div class="service" style="left:420px;top:632px">
    <div class="service-head"><span class="service-icon"><svg width="20" height="20" viewBox="0 0 20 20" fill="none" stroke="var(--teal)" stroke-width="1.6"><rect x="4" y="2" width="12" height="16"/><path d="M7 6h6M7 9h6M7 12h4"/></svg></span>KEV Preparation</div>
    <p>We provide specialized and effective small group KEV preparation classes starting from 8th grade to realize students dream colleges.</p>
  </div>
  <div class="service" style="left:420px;top:738px">
    <div class="service-head"><span class="service-icon"><svg width="20" height="20" viewBox="0 0 20 20" fill="none" stroke="var(--teal)" stroke-width="1.6"><rect x="2" y="3" width="16" height="11"/><path d="M7 17h6M10 14v3"/></svg></span>Computer Science</div>
    <p>Exposing students to computer science in early ages improves their understanding of technology, which makes them not only users of technology but also innovators of next generation technology</p>
  </div>
  <div class="service" style="left:420px;top:844px">
    <div class="service-head"><span class="service-icon"><svg width="20" height="20" viewBox="0 0 20 20" fill="none" stroke="var(--teal)" stroke-width="1.6"><rect x="3" y="3" width="14" height="14"/><path d="M8 3v14M12 3v14"/></svg></span>Custom Courses</div>
    <p>We offer individually tailored courses to meet varying needs of students, whether it is a one-on-one tutoring or special subject tutoring. QN Academy has experienced teachers to help you in any academic subject.</p>
  </div>

  <div class="footer">
    <div class="footer-cell">1480 Maple Ridge Road Suite #210<br>Cedar Falls, GA 30000</div>
    <div class="footer-phone">555-014-2290</div>
    <div class="footer-cell footer-web">customerservice@qnacademyga.com<br>w w w . q n a c a d e m y g a . c o m</div>
  </div>
</section>

</body>
</html>
```